Antigen Preservation Bureau

The company will provide a contract research services to stabilize various viruses, viral vectors, and vaccines. It may offer some licensing opportunities for stabilizing technologies. Main area of applications are pharmaceutical, therapeutic, and vaccination field. The company aspires to develop room temperature vaccines for global distribution beyond the current cold chain.

Target Market(s)

pharmaceutical, therapeutic and vaccination fields

Coding

Coded - Design and coding required

Number of Pages Required

4 page

Requirements
Must have
• Incorporate a APB logo, attached at the bottom, on the Web page

```html
<!DOCTYPE html>
<html lang="en">
<head>
<meta charset="utf-8">
<title>Antigen Preservation Bureau</title>
<link href="https://fonts.googleapis.com/css2?family=Roboto:wght@300;400;500;700&display=swap" rel="stylesheet">
<style>
:root{
  --gold:#c99b45;
  --teal:#2f8c74;
  --ink:#1c1c1c;
  --text:#666;
  --muted:#9a9a9a;
  --soft:#f3f3f3;
  --line:#e2e2e2;
  --white:#fff;
}
*{box-sizing:border-box;margin:0;padding:0}
html,body{width:1200px;height:3158px;overflow:hidden}
body{position:relative;background:var(--white);font-family:'Roboto',sans-serif;color:var(--text)}
.abs{position:absolute}

.topbar{left:0;top:0;width:1200px;height:30px;background:var(--gold)}
.topbar .social{position:absolute;right:56px;top:8px;display:flex;gap:12px}
.topbar .social span{width:14px;height:14px;border-radius:50%;background:var(--white);opacity:.9}

.brand{display:flex;align-items:center;gap:12px}
.brand .mark{width:44px;height:44px;border-radius:50%;background:var(--teal)}
.brand .name{font-weight:500;color:var(--teal);font-size:15px;letter-spacing:2px;line-height:1.25;text-transform:uppercase}
.header-brand{left:0;width:1200px;top:48px;justify-content:center}

.nav{left:2px;top:128px;width:1196px;height:40px;border:1px solid var(--line);display:flex;justify-content:center;align-items:center;gap:46px;font-size:10px;color:#555}
.nav a{display:flex;align-items:center;gap:5px;text-decoration:none;color:inherit}
.nav a i{width:9px;height:9px;border:1.3px solid var(--gold);border-radius:2px;display:block}
.nav a.active{color:var(--gold)}

.hero{left:162px;top:200px;width:876px;height:373px;background:linear-gradient(135deg,#f1f3f6 0%,#e3e7ec 60%,#d6dce2 100%);box-shadow:0 14px 14px -10px rgba(0,0,0,.35)}

.kicker{font-size:10px;color:#555;text-align:center}
.title{font-size:26px;font-weight:700;color:var(--ink);text-align:center;letter-spacing:.3px}
.rule{width:26px;height:3px;background:var(--teal);margin:8px auto 0}
.center-head{left:0;width:1200px}

.service{top:730px;width:276px;height:253px;background:var(--soft);border:1px solid var(--line)}
.service .icon{position:absolute;left:112px;top:14px;width:52px;height:52px;border-radius:50%;background:var(--white);box-shadow:0 1px 4px rgba(0,0,0,.2);display:flex;align-items:center;justify-content:center}
.service .photo{position:absolute;left:0;top:80px;width:274px;height:116px}
.service .label{position:absolute;left:0;width:274px;top:216px;text-align:center;font-size:16px;color:var(--ink)}
.service .label.accent{color:var(--gold);font-weight:500}

.about{left:162px;top:1042px;width:876px;height:267px;background:var(--gold);color:var(--white)}
.about .head{position:absolute;left:50px;top:103px}
.about .head small{font-size:10px;display:block}
.about .head h2{font-size:26px;font-weight:700;margin-top:2px}
.about .head .rule{margin:6px 0 0;background:var(--white)}
.about .divider{position:absolute;left:215px;top:46px;width:1px;height:175px;background:rgba(255,255,255,.55)}
.about .copy{position:absolute;left:250px;top:42px;width:590px;font-size:10.5px;line-height:19px}
.about .copy p+p{margin-top:13px}

.focus-band{left:0;top:1370px;width:1200px;height:489px;background:var(--soft)}
.intro{left:310px;top:1505px;width:580px;font-size:11px;line-height:20px;text-align:center;color:var(--muted)}
.orb{top:1602px;width:190px;height:190px;border-radius:50%;display:flex;align-items:flex-end;justify-content:center;padding-bottom:32px;color:var(--white);font-weight:700;font-size:16px}

.team-text{left:162px;top:1916px;width:360px}
.team-text small{font-size:10px;color:#555}
.team-text h2{font-size:26px;font-weight:700;color:var(--ink);margin-top:2px}
.team-text .rule{margin:6px 0 0}
.team-text p{margin-top:30px;font-size:11px;line-height:22px}
.btn{display:inline-block;border:1.5px solid var(--teal);color:var(--teal);font-size:9px;font-weight:700;border-radius:14px;padding:6px 18px;letter-spacing:.3px}
.team-text .btn{margin-top:28px}
.slider{left:600px;top:1918px;width:438px;height:299px;background:linear-gradient(135deg,#8a8a8a 0%,#4a4a4a 55%,#2e2e2e 100%)}
.slider .arrow{position:absolute;top:136px}
.slider .caption{position:absolute;left:0;width:438px;top:220px;text-align:center;color:var(--white);font-size:12px;font-weight:700}
.slider .caption span{display:block;font-weight:300;font-size:11px;margin-top:4px}
.slider .dots{position:absolute;left:0;width:438px;top:270px;display:flex;justify-content:center;gap:7px}
.slider .dots i{width:6px;height:6px;border-radius:50%;background:rgba(255,255,255,.55)}
.slider .dots i:first-child{background:var(--white)}

.news-band{left:0;top:2278px;width:1200px;height:579px;background:var(--soft)}
.post{top:2436px;width:276px;height:360px;background:var(--white);box-shadow:0 2px 8px rgba(0,0,0,.08)}
.post .photo{height:149px}
.post .body{padding:14px 22px}
.post .date{font-size:10px;color:var(--ink);font-weight:500;display:flex;align-items:center;gap:8px}
.post .date i{width:10px;height:10px;background:var(--gold);border-radius:2px;display:block}
.post p{font-size:10.5px;line-height:19px;margin-top:13px}
.post .btn{margin-top:18px}
.post .link{margin-top:18px;font-size:9px;font-weight:700;color:var(--teal);padding:6px 0;display:inline-block}

.footer-brand{left:162px;top:2918px}
.footer-links{left:461px;top:2918px;list-style:none;font-size:9.5px;line-height:22px;text-transform:uppercase;color:#777}
.footer-col{top:2916px;font-size:10px;line-height:20px}
.footer-col h4{font-size:12px;color:var(--ink);font-weight:700;margin-bottom:10px}
.footer-col a{color:var(--gold);text-decoration:none}
.follow span{display:block;width:24px;height:24px;border-radius:50%;border:1.5px solid #888;margin-bottom:8px}
.follow span:first-of-type{background:var(--teal);border-color:var(--teal)}
.footer-rule{left:162px;top:3105px;width:876px;height:1px;background:var(--line)}
.copyright{left:162px;top:3124px;font-size:9.5px;color:var(--muted)}
</style>
</head>
<body>

<div class="abs topbar">
  <div class="social"><span></span><span></span><span></span><span></span></div>
</div>

<div class="abs brand header-brand">
  <span class="mark"></span>
  <span class="name">Antigen<br>Preservation<br>Bureau</span>
</div>

<nav class="abs nav">
  <a class="active"><i></i>Home</a>
  <a><i></i>About Us</a>
  <a><i></i>Our Services</a>
  <a><i></i>Our Technologies</a>
  <a><i></i>Partners</a>
  <a><i></i>News</a>
  <a><i></i>Contact Us</a>
</nav>

<div class="abs hero" role="img" aria-label="Syringe lying beside a small vial and a glass vaccine bottle on a white surface"></div>

<div class="abs center-head" style="top:634px">
  <div class="kicker">What We Do</div>
  <div class="title">OUR SERVICES</div>
  <div class="rule"></div>
</div>

<div class="abs service" style="left:162px">
  <div class="icon"><svg width="22" height="22" viewBox="0 0 22 22"><rect x="3" y="8" width="16" height="6" rx="3" transform="rotate(-45 11 11)" fill="none" stroke="#c99b45" stroke-width="2"/></svg></div>
  <div class="photo" role="img" aria-label="Assorted pills and capsules spilling from a wooden spoon" style="background:linear-gradient(120deg,#9fd3e6,#d9a06a 55%,#8cc8e0)"></div>
  <div class="label accent">Pharmaceutical</div>
</div>
<div class="abs service" style="left:461px">
  <div class="icon"><svg width="22" height="22" viewBox="0 0 22 22"><circle cx="11" cy="7" r="3" fill="#2f8c74"/><circle cx="5" cy="14" r="2.5" fill="#1c1c1c"/><circle cx="17" cy="14" r="2.5" fill="#1c1c1c"/></svg></div>
  <div class="photo" role="img" aria-label="Microscopic blue bacteria" style="background:linear-gradient(120deg,#0c3f78,#1e78b8 50%,#0a3466)"></div>
  <div class="label">Therapeutic</div>
</div>
<div class="abs service" style="left:762px">
  <div class="icon"><svg width="22" height="22" viewBox="0 0 22 22"><rect x="8" y="4" width="6" height="14" rx="1" fill="none" stroke="#c99b45" stroke-width="2"/><rect x="8" y="12" width="6" height="6" fill="#2f8c74"/></svg></div>
  <div class="photo" role="img" aria-label="Syringe and vaccine vials on a green background" style="background:linear-gradient(120deg,#6f9a5c,#c6d6c0 55%,#5e8a52)"></div>
  <div class="label">Vaccination</div>
</div>

<section class="abs about">
  <div class="head">
    <small>Who We Are</small>
    <h2>ABOUT US</h2>
    <div class="rule"></div>
  </div>
  <div class="divider"></div>
  <div class="copy">
    <p>Sed ut perspiciatis unde omnis iste natus error sit voluptatem accusantium doloremque laudantium, totam rem aperiam, eaque ipsa quae ab illo inventore veritatis et quasi architecto beatae vitae dicta sunt explicabo. Nemo enim ipsam voluptatem quia voluptas sit aspernatur aut odit aut fugit, sed quia consequuntur magni dolores eos qui ratione voluptatem sequi nesciunt. Neque porro quisquam est, qui dolorem ipsum quia dolor sit amet, consectetur, adipisci velit, sed quia non numquam eius modi tempora incidunt ut labore et dolore magnam aliquam quaerat voluptatem.</p>
    <p>Lorem ipsum dolor sit amet, consectetur adipiscing elit, sed do eiusmod tempor incididunt ut labore et dolore magna aliqua. Ut enim ad minim veniam, quis nostrud exercitation ullamco laboris nisi ut aliquip ex ea commodo consequat ad minima veniam, quis nostrum exercitationem.</p>
  </div>
</section>

<div class="abs focus-band"></div>
<div class="abs center-head" style="top:1428px">
  <div class="kicker">Research Services</div>
  <div class="title">FOCUS</div>
  <div class="rule"></div>
</div>
<p class="abs intro">Sed ut perspiciatis unde omnis iste natus error sit voluptatem accusantium doloremque laudantium, totam rem aperiam, eaque ipsa quae ab illo inventore veritatis et quasi architecto beatae vitae dicta sunt explicabo. Nemo enim ipsam voluptatem quia voluptas sit aspernatur aut odit aut fugit, sed quia.</p>

<div class="abs orb" style="left:294px;background:radial-gradient(circle at 40% 35%,#5f9bd8,#1a3f7a 60%,#0b1f44)" role="img" aria-label="Blue neuron-like virus cell">VIRUSES</div>
<div class="abs orb" style="left:505px;background:radial-gradient(circle at 50% 40%,#6fe0e0,#1b8fa8 55%,#0c3556)" role="img" aria-label="Spiky teal viral particle">VIRAL VECTOR</div>
<div class="abs orb" style="left:715px;background:radial-gradient(circle at 40% 40%,#c9d8e4,#6f8ea8 55%,#2f4a63)" role="img" aria-label="Gloved hand holding a vaccine vial">VACCINES</div>

<div class="abs team-text">
  <small>What We Do</small>
  <h2>MEET THE TEAM</h2>
  <div class="rule"></div>
  <p>Lorem ipsum dolor sit amet, consectetur adipiscing elit, sed do eiusmod tempor incididunt ut labore et dolore magna aliqua. Ut enim ad minim veniam, quis nostrud exercitation ullamco laboris nisi ut aliquip ex ea commodo consequat. Duis aute irure dolor in reprehenderit in voluptate velit esse cillum dolore eu fugiat nulla pariatur. Excepteur sint occaecat cupidatat non</p>
  <span class="btn">READ MORE</span>
</div>

<div class="abs slider" role="img" aria-label="Portrait of a smiling team member in a dark suit">
  <svg class="arrow" style="left:16px" width="12" height="20" viewBox="0 0 12 20"><path d="M10 2 2 10l8 8" fill="none" stroke="#fff" stroke-width="2"/></svg>
  <svg class="arrow" style="right:16px" width="12" height="20" viewBox="0 0 12 20"><path d="M2 2l8 8-8 8" fill="none" stroke="#fff" stroke-width="2"/></svg>
  <div class="caption">Team Member Name<span>Position</span></div>
  <div class="dots"><i></i><i></i><i></i><i></i><i></i><i></i><i></i></div>
</div>

<div class="abs news-band"></div>
<div class="abs center-head" style="top:2333px">
  <div class="kicker">Whats new?</div>
  <div class="title">LATEST NEWS</div>
  <div class="rule"></div>
</div>

<article class="abs post" style="left:162px">
  <div class="photo" role="img" aria-label="Green spherical virus particles" style="background:radial-gradient(circle at 40% 50%,#7fc8a8,#2f7a8a 55%,#1b4a6a)"></div>
  <div class="body">
    <div class="date"><i></i>28 December, 2018</div>
    <p>Lorem ipsum dolor sit amet, consectetur adipiscing elit, sed do eiusmod tempor incididunt ut labore et dolore magna aliqua. Ut enim ad minim veniam, quis nostrud exercitation ullamco laboris nisi ut aliquip ex ea commodo consequat.</p>
    <span class="btn">READ MORE</span>
  </div>
</article>
<article class="abs post" style="left:461px">
  <div class="photo" role="img" aria-label="Glass vials and a syringe on a table" style="background:linear-gradient(135deg,#e6ebef,#b5c0c8 55%,#8b99a4)"></div>
  <div class="body">
    <div class="date"><i></i>01 January, 2019</div>
    <p>Lorem ipsum dolor sit amet, consectetur adipiscing elit, sed do eiusmod tempor incididunt ut labore et dolore magna aliqua. Ut enim ad minim veniam, quis nostrud exercitation ullamco laboris nisi ut aliquip ex ea commodo consequat.</p>
    <span class="link">READ MORE</span>
  </div>
</article>
<article class="abs post" style="left:762px">
  <div class="photo" role="img" aria-label="Researchers in lab coats seated at a meeting table" style="background:linear-gradient(135deg,#d9dfe4,#a6b0b8 50%,#e8ecef)"></div>
  <div class="body">
    <div class="date"><i></i>5 January, 2019</div>
    <p>Lorem ipsum dolor sit amet, consectetur adipiscing elit, sed do eiusmod tempor incididunt ut labore et dolore magna aliqua. Ut enim ad minim veniam, quis nostrud exercitation ullamco laboris nisi ut aliquip ex ea commodo consequat.</p>
    <span class="link">READ MORE</span>
  </div>
</article>

<footer>
  <div class="abs brand footer-brand">
    <span class="mark"></span>
    <span class="name">Antigen<br>Preservation<br>Bureau</span>
  </div>
  <ul class="abs footer-links">
    <li>Home</li><li>About Us</li><li>Our Services</li><li>Our Technologies</li><li>Partners</li><li>News</li><li>Contact Us</li>
  </ul>
  <div class="abs footer-col" style="left:655px;width:200px">
    <h4>ADDRESS</h4>
    <div>Lorem ipsum dolor sit amet,<br>consectetur adipiscing elit 4-8<br>012345 sed do eiusmod, tempor<br>+123 456 7890</div>
    <div style="margin-top:10px"><a>info@antigenpreservationbureau.org</a></div>
  </div>
  <div class="abs footer-col follow" style="left:911px">
    <h4>FOLLOW US</h4>
    <span></span><span></span><span></span><span></span>
  </div>
  <div class="abs footer-rule"></div>
  <div class="abs copyright">© 2018 APB. All rights reserved.</div>
</footer>

</body>
</html>
```